Vantor Advisory business card

Premium business card required
I have attached the brand as a powerpoint template but this can be made to look very up market, I have also attached my BIO for title reasons and to give you a feel for my skills
front of card
Derek Holloway
Managing Director Vantor Advisory
Retail, Customer-Led Experience, Transformation and Maximising Shareholder Return
Mobile +61(0)418557392
Email derekvantoradvisory.com
back of card

VANTOR ADVISORY’ OFFERING

We transform customer environments to extract benefits while elevating service levels;
We release millions of dollars in self-funding through continuous improvement;
We see CX as a key differentiator, proactively guarding share from market disrupters;
We re-invent service and create front-end of the future.

```html
<!DOCTYPE html>
<html lang="en">
<head>
<meta charset="utf-8">
<title>Vantor Advisory Business Card</title>
<link rel="stylesheet" href="https://fonts.googleapis.com/css2?family=Montserrat:wght@400;500;600&display=swap">
<style>
  :root {
    --stage: #2f2925;
    --card: #ffffff;
    --accent-grey: #8c8c8c;
    --text-dark: #3a3a3a;
    --decor: #f1f1f2;
  }
  * { box-sizing: border-box; margin: 0; padding: 0; }
  html, body { width: 1200px; height: 715px; overflow: hidden; }
  body {
    background: var(--stage);
    font-family: "Montserrat", sans-serif;
    display: flex;
    align-items: center;
    justify-content: center;
    gap: 56px;
  }
  .card {
    position: relative;
    width: 525px;
    height: 300px;
    background: var(--card);
    overflow: hidden;
    box-shadow: 0 12px 30px rgba(0,0,0,0.45);
  }
  .card__decor {
    position: absolute;
    right: 40px;
    top: 40px;
    width: 220px;
    height: 220px;
    background: var(--decor);
  }
  .brand {
    position: absolute;
    left: 34px;
    top: 30px;
    display: flex;
    align-items: center;
    gap: 10px;
  }
  .brand__square {
    width: 18px;
    height: 18px;
    background: var(--accent-grey);
  }
  .brand__name {
    font-size: 24px;
    font-weight: 600;
    color: var(--accent-grey);
    letter-spacing: 0.5px;
  }
  .offering {
    position: absolute;
    left: 34px;
    top: 96px;
    right: 30px;
  }
  .offering__title {
    font-size: 13px;
    font-weight: 500;
    color: var(--accent-grey);
    letter-spacing: 0.3px;
    margin-bottom: 14px;
  }
  .offering__list { list-style: none; }
  .offering__item {
    position: relative;
    padding-left: 12px;
    font-size: 10.5px;
    line-height: 1.55;
    color: var(--text-dark);
  }
  .offering__item::before {
    content: "";
    position: absolute;
    left: 0;
    top: 6px;
    width: 5px;
    height: 5px;
    border-radius: 50%;
    background: var(--accent-grey);
  }
  .contact {
    position: absolute;
    left: 34px;
    top: 110px;
  }
  .contact__name {
    font-size: 19px;
    font-weight: 500;
    color: var(--accent-grey);
    letter-spacing: 0.5px;
    text-transform: uppercase;
  }
  .contact__role, .contact__company {
    font-size: 14px;
    color: var(--text-dark);
    line-height: 1.35;
  }
  .contact__lines { margin-top: 14px; }
  .contact__line {
    display: flex;
    align-items: center;
    gap: 10px;
    font-size: 14px;
    color: var(--text-dark);
    line-height: 1.5;
  }
  .contact__icon { width: 11px; height: 11px; fill: none; stroke: var(--accent-grey); stroke-width: 1.4; }
</style>
</head>
<body>
  <section class="card card--back">
    <div class="card__decor"></div>
    <div class="brand">
      <span class="brand__square"></span>
      <span class="brand__name">Vantor Advisory</span>
    </div>
    <div class="offering">
      <h2 class="offering__title">VANTOR ADVISORY’ OFFERING</h2>
      <ul class="offering__list">
        <li class="offering__item">We transform customer environments to extract benefits while elevating service levels;</li>
        <li class="offering__item">We release millions of dollars in self-funding through continuous improvement;</li>
        <li class="offering__item">We see CX as a key differentiator, proactively guarding share from market disrupters;</li>
        <li class="offering__item">We re-invent service and create front-end of the future.</li>
      </ul>
    </div>
  </section>

  <section class="card card--front">
    <div class="card__decor"></div>
    <div class="brand">
      <span class="brand__square"></span>
      <span class="brand__name">Vantor Advisory</span>
    </div>
    <div class="contact">
      <h1 class="contact__name">Derek Holloway</h1>
      <p class="contact__role">Managing Director</p>
      <p class="contact__company">Vantor Advisory</p>
      <div class="contact__lines">
        <p class="contact__line">
          <svg class="contact__icon" viewBox="0 0 12 12" aria-hidden="true"><path d="M2.5 1.5 L4.5 1.5 L5.2 4 L4 5 Q5 7.2 7 8 L8 6.8 L10.5 7.5 L10.5 9.5 Q6 10.5 2.5 6 Q1.5 3.5 2.5 1.5 Z"/></svg>
          +61(0)418557392
        </p>
        <p class="contact__line">
          <svg class="contact__icon" viewBox="0 0 12 12" aria-hidden="true"><rect x="1" y="2.5" width="10" height="7"/><path d="M1 2.5 L6 6.5 L11 2.5"/></svg>
          derekvantoradvisory.com
        </p>
      </div>
    </div>
  </section>
</body>
</html>
```